User-interface and web design for new forum-style communication platform

We developed a new forum-style communication platform specially targetting stock investors to share and discuss information on companies listed on the stock exchange.

You have complete freedom for designing the user-interface and web design. Designs should include all features listed below.

Please read the attached document for full specifications. Also attached is a mockup of the layout, but this is only directional. A mockup for the user-profile is also attached, but does not need to be designed.

This project focusses on the homepage and thread view.

The winner(s) will be asked to design the complete project. (create thread box, user profile, registering, settings...)

We are looking for a well thought out, smart design that incorporates the specifications in the attached document. Please do not hesitate to contact us if anything is not clear.

Target Market(s)

Stock investors from 25 to 60 years old (the people that are currently on investor forums)

Industry/Entity Type

Communication

Font styles to use
Sans Serif

Colors

Designer to choose colors to be used in the design.

Requirements
Must have
• Full homepage design & Thread view specified in the attached document.
Nice to have
• Create thread view
- Field for adding tags
- field for subject of the thread
- text box with basic text editing
- method for sharing media
Should not have
• Logo design.

```html
<!DOCTYPE html>
<html lang="en">
<head>
<meta charset="utf-8">
<title>Ticker Commons – Conversations</title>
<link href="https://fonts.googleapis.com/css2?family=Lato:wght@400;700&family=Oswald:wght@500&display=swap" rel="stylesheet">
<style>
:root{
  --blue:#2f8fd5;
  --blue-dark:#2a7fc0;
  --navy:#3a5577;
  --navy-text:#35506f;
  --page:#e4e3e1;
  --panel:#f1f1f1;
  --line:#dcdcdc;
  --text:#333;
  --muted:#666;
  --white:#fff;
}
*{box-sizing:border-box;margin:0;padding:0}
html,body{width:1200px;height:1132px;overflow:hidden}
body{position:relative;background:var(--page);font-family:'Lato',sans-serif;color:var(--text);font-size:13px}
.abs{position:absolute}

/* header */
.site-header{position:absolute;left:0;top:0;width:1200px;height:94px;background:var(--blue)}
.brand{position:absolute;left:131px;top:22px;font-family:'Oswald',sans-serif;font-weight:500;font-size:40px;line-height:48px;color:var(--white);letter-spacing:.3px}
.notice{position:absolute;left:842px;top:11px;width:103px;height:25px;background:var(--white);border-radius:2px;color:var(--navy-text);font-size:12px;line-height:25px;text-align:center}
.notice:after{content:"";position:absolute;right:-6px;top:7px;border:6px solid transparent;border-right:0;border-left-color:var(--white)}
.badge{position:absolute;left:957px;top:9px;width:28px;height:28px;border-radius:50%;background:var(--navy);border:2px solid #cfd8e3;color:var(--white);font-size:16px;line-height:24px;text-align:center}
.user-menu{position:absolute;left:997px;top:11px;width:72px;height:24px;display:flex;border-radius:2px;overflow:hidden}
.user-menu span{flex:1;background:#dde3ea;color:var(--muted);font-size:13px;line-height:24px;text-align:center}
.user-menu i{width:22px;background:var(--navy);display:flex;align-items:center;justify-content:center}
.search-bar{position:absolute;left:637px;top:50px;width:432px;height:33px;background:#e9eef3;border-radius:3px}
.search-bar .field{position:absolute;left:4px;top:3px;width:283px;height:27px;background:var(--white);border-radius:2px;font-size:13px;color:#555;line-height:27px;padding-left:34px}
.search-bar .field svg{position:absolute;left:11px;top:6px}
.btn{position:absolute;height:27px;border-radius:2px;color:var(--white);font-weight:700;font-size:14px;line-height:27px;text-align:center}
.btn-save{left:291px;top:3px;width:66px;background:var(--navy)}
.btn-clear{left:362px;top:3px;width:66px;background:var(--blue)}

/* sidebar */
.sidebar{position:absolute;left:131px;top:136px;width:281px}
.widget-head{position:absolute;left:0;width:281px;height:33px;background:var(--blue);color:var(--white);font-size:17px;line-height:33px;padding-left:48px}
.widget-head .ico{position:absolute;left:0;top:0;width:38px;height:33px;background:#4ea2e0;display:flex;align-items:center;justify-content:center}
.side-search{position:absolute;left:13px;width:254px;height:32px;background:var(--white);border:1px solid #d8d8d8;font-size:13px;color:#666;line-height:30px;padding-left:10px}
.side-search svg{position:absolute;right:9px;top:7px}
.list{position:absolute;left:0;width:281px;background:var(--panel)}
.list li{list-style:none;height:39px;border-bottom:2px solid #e2e2e2;font-size:14px;line-height:39px;padding-left:35px;position:relative}
.list li:before{content:"";position:absolute;left:23px;top:15px;border:4px solid transparent;border-right:0;border-left:5px solid #bbb}
.list .show-all{height:37px;line-height:37px;padding-left:22px;font-size:13px;color:var(--navy-text);border-bottom:2px solid #e6e6e6;background:#ebebeb}
.list .show-all:before{display:none}
.list .spacer{height:30px;border:0;background:var(--panel)}
.list .spacer:before{display:none}
.dots{display:inline-block;vertical-align:middle;margin-left:3px}

/* main */
.main{position:absolute;left:441px;top:136px;width:628px;height:886px;background:var(--white)}
.main-top{position:absolute;left:0;top:0;width:628px;height:75px;background:var(--blue)}
.crumbs{position:absolute;left:13px;top:12px;font-size:12.5px;color:var(--white)}
.btn-create{position:absolute;left:482px;top:24px;width:132px;height:28px;background:var(--navy);border-radius:2px;color:var(--white);font-weight:700;font-size:14px;line-height:28px;padding-left:36px}
.btn-create svg{position:absolute;left:10px;top:6px}
.tab{position:absolute;top:42px;width:84px;height:33px;background:var(--navy);color:var(--white);font-size:14px;line-height:33px;text-align:center;border-radius:3px 3px 0 0}
.tab.active{background:#eef0f2;color:var(--navy-text);height:33px}

.thread{position:absolute;left:13px;width:601px}
.thread-bar{position:absolute;left:0;top:0;width:601px;height:33px;background:var(--blue);color:var(--white);font-size:14px;line-height:33px;padding-left:16px}
.thread-body{position:absolute;left:0;top:33px;width:601px;height:180px;background:var(--panel)}
.avatar{position:absolute;left:10px;top:14px;width:94px;height:92px;background:var(--white);border:1px solid #ddd;padding:3px}
.avatar div{width:100%;height:100%}
.thread-title{position:absolute;left:123px;top:10px;font-weight:700;font-size:15px;color:#333}
.meta{position:absolute;left:123px;top:41px;font-size:11.5px;color:#555}
.meta b{font-weight:400;color:var(--blue);font-size:13px;margin-left:3px}
.excerpt{position:absolute;left:124px;top:66px;width:470px;font-size:13.2px;line-height:18.4px;color:#444}
.more{position:absolute;left:123px;top:153px;font-weight:700;font-size:12px;color:var(--navy-text)}
.stats{position:absolute;left:0;top:213px;width:601px;height:53px;background:#ebebeb}
.stat{position:absolute;top:18px;font-size:13.5px;color:#333;display:flex;align-items:center;gap:8px}
.act{position:absolute;top:12px;height:28px;border-radius:2px;background:var(--navy);color:var(--white);font-size:14px;line-height:28px;display:flex;align-items:center;justify-content:center;gap:8px}
.act.hot{background:var(--blue)}
.reply{position:absolute;left:0;top:276px;width:601px;height:83px;border-left:4px solid #e1e1e1}
.reply .ph{position:absolute;left:10px;top:0;width:56px;height:56px;background:#f0f0f0;border:1px solid #e6e6e6;display:flex;align-items:flex-end;justify-content:center}
.reply .box{position:absolute;left:75px;top:0;width:522px;height:83px;background:#f3f4f4;border:1px solid #ececec;font-size:12.5px;color:#777;padding:6px 9px}

.dropdown{position:absolute;background:var(--white);box-shadow:0 1px 4px rgba(0,0,0,.25);border-radius:2px;padding:3px 0}
.dropdown div{height:22px;line-height:22px;font-size:13.5px;padding-left:19px;position:relative;color:#333}
.dropdown div:before{content:"";position:absolute;left:8px;top:7px;border:4px solid transparent;border-right:0;border-left:5px solid #bbb}
.dropdown .on{background:var(--blue);color:var(--white)}
.dropdown .on:before{border-left-color:var(--white)}

/* footer */
.top-tab{position:absolute;left:559px;top:1055px;width:86px;height:44px;border-radius:43px 43px 0 0;background:#ededed;font-size:12px;font-weight:700;color:#666;text-align:center;line-height:36px}
.site-footer{position:absolute;left:0;top:1084px;width:1200px;height:48px;background:#ededed;border-top:1px solid #ddd}
.copy{position:absolute;left:133px;top:16px;font-size:13px;color:#555}
.social{position:absolute;top:12px;width:23px;height:23px;border-radius:2px}
</style>
</head>
<body>

<header class="site-header">
  <div class="brand">Ticker Commons</div>
  <div class="notice">1 New Follower</div>
  <div class="badge">3</div>
  <div class="user-menu"><span>User</span><i><svg width="10" height="7" viewBox="0 0 10 7"><path d="M1 1l4 4 4-4" stroke="#fff" stroke-width="2" fill="none"/></svg></i></div>
  <div class="search-bar">
    <div class="field"><svg width="15" height="15" viewBox="0 0 15 15"><circle cx="6" cy="6" r="4.5" stroke="#555" stroke-width="2" fill="none"/><path d="M9.5 9.5l4 4" stroke="#555" stroke-width="2"/></svg>#vantra #heliox</div>
    <div class="btn btn-save">Save</div>
    <div class="btn btn-clear">Clear</div>
  </div>
</header>

<aside class="sidebar">
  <div class="widget-head" style="top:0"><span class="ico"><svg width="17" height="17" viewBox="0 0 17 17"><circle cx="8.5" cy="5" r="4" fill="#fff"/><path d="M1 17c0-5 3-7 7.5-7s7.5 2 7.5 7z" fill="#fff"/></svg></span>Users</div>
  <div class="side-search" style="top:49px">Search<svg width="17" height="17" viewBox="0 0 17 17"><circle cx="7" cy="7" r="5.5" stroke="#3a5577" stroke-width="2.2" fill="none"/><path d="M11 11l5 5" stroke="#3a5577" stroke-width="2.4"/></svg></div>

  <div class="widget-head" style="top:100px"><span class="ico"><svg width="14" height="17" viewBox="0 0 14 17"><rect x="1" y="1" width="12" height="15" rx="1" fill="none" stroke="#fff" stroke-width="2"/><circle cx="7" cy="7" r="2" fill="#fff"/><rect x="4" y="10" width="6" height="3" fill="#fff"/></svg></span>Saved Filters</div>
  <ul class="list" style="top:133px">
    <li>Item One</li><li>Item Two</li><li>Item Three</li>
    <li class="show-all">Show all <svg class="dots" width="8" height="8" viewBox="0 0 8 8" fill="#35506f"><rect width="3" height="3"/><rect x="5" width="3" height="3"/><rect y="5" width="3" height="3"/><rect x="5" y="5" width="3" height="3"/></svg></li>
    <li class="spacer"></li>
  </ul>

  <div class="widget-head" style="top:324px"><span class="ico"><svg width="17" height="17" viewBox="0 0 17 17"><path d="M1 1h7l8 8-7 7-8-8z" fill="#fff"/><circle cx="5" cy="5" r="1.6" fill="#4ea2e0"/></svg></span>Popular Tage</div>
  <ul class="list" style="top:357px">
    <li>Item One</li><li>Item Two</li><li>Item Three</li>
    <li class="show-all">Show all <svg class="dots" width="8" height="8" viewBox="0 0 8 8" fill="#35506f"><rect width="3" height="3"/><rect x="5" width="3" height="3"/><rect y="5" width="3" height="3"/><rect x="5" y="5" width="3" height="3"/></svg></li>
    <li class="spacer"></li>
  </ul>

  <div class="widget-head" style="top:548px"><span class="ico"><svg width="17" height="17" viewBox="0 0 17 17"><rect x="5" y="1" width="11" height="11" fill="none" stroke="#fff" stroke-width="1.8"/><path d="M3 5H1v11h11v-2" fill="none" stroke="#fff" stroke-width="1.8"/></svg></span>Popular Contributors</div>
  <ul class="list" style="top:581px">
    <li>Item One</li><li>Item Two</li><li>Item Three</li>
    <li class="show-all">Show all <svg class="dots" width="8" height="8" viewBox="0 0 8 8" fill="#35506f"><rect width="3" height="3"/><rect x="5" width="3" height="3"/><rect y="5" width="3" height="3"/><rect x="5" y="5" width="3" height="3"/></svg></li>
  </ul>
</aside>

<main class="main">
  <div class="main-top">
    <div class="crumbs">Home &nbsp;» Conversations » Public #vantra#heliox</div>
    <div class="btn-create"><svg width="17" height="17" viewBox="0 0 17 17"><path d="M2 15l1-4 9-9 3 3-9 9z" fill="#fff"/></svg>Create Thread</div>
    <div class="tab active" style="left:14px">Public</div>
    <div class="tab" style="left:104px">Following</div>
    <div class="tab" style="left:194px">Contacts</div>
  </div>

  <!-- thread 1 -->
  <article class="thread" style="top:104px">
    <div class="thread-bar"></div>
    <div class="thread-body">
      <div class="avatar"><div role="img" aria-label="Member photo" style="background:linear-gradient(160deg,#b9c3cc,#3b4450)"></div></div>
      <div class="thread-title">Lorem ipsum dolor sit amet conse ctetuer adipiscing elit.</div>
      <div class="meta">Posted by Martin Hale on <b>01/01/2014 - 15:32</b></div>
      <p class="excerpt">Lorem ipsum dolor sit actetuer adipiscing elitsed diam nonummy nibh euismodi tincidunt ut laoreet dolore magna aliquam erat volutpat. wisi eniminim veniamr quis nostrud exerci tation ullcorper suscipit lobortis nisl ut aliquip ea commodo consequat obortis nisl ut aliquip ea commodo consequat.</p>
      <div class="more">READ MORE »</div>
    </div>
    <div class="stats">
      <div class="stat" style="left:13px"><svg width="22" height="13" viewBox="0 0 22 13"><path d="M1 6.5C5 0 17 0 21 6.5 17 13 5 13 1 6.5z" fill="#3a5577"/><circle cx="11" cy="6.5" r="3.2" fill="#ebebeb"/><circle cx="11" cy="6.5" r="1.8" fill="#3a5577"/></svg>250 views</div>
      <div class="stat" style="left:118px"><svg width="19" height="17" viewBox="0 0 19 17"><path d="M1 1h17v11H7l-4 4v-4H1z" fill="#3a5577"/><path d="M4 4.5h11M4 8h8" stroke="#ebebeb" stroke-width="1.4"/></svg>12 replies</div>
      <div class="act hot" style="left:335px;width:81px"><svg width="14" height="11" viewBox="0 0 14 11"><path d="M6 0L0 5l6 5V7c4 0 6 1 8 4 0-5-3-7-8-7z" fill="#fff"/></svg>Reply</div>
      <div class="act" style="left:422px;width:85px"><svg width="15" height="15" viewBox="0 0 15 15"><circle cx="3" cy="7.5" r="2.3" fill="#fff"/><circle cx="12" cy="2.5" r="2.3" fill="#fff"/><circle cx="12" cy="12.5" r="2.3" fill="#fff"/><path d="M3 7.5l9-5M3 7.5l9 5" stroke="#fff" stroke-width="1.5"/></svg>Share</div>
      <div class="act" style="left:513px;width:110px;width:103px"><svg width="17" height="16" viewBox="0 0 17 16"><path d="M8.5 0l2.6 5.3 5.9.8-4.3 4.1 1 5.8-5.2-2.8-5.2 2.8 1-5.8L0 6.1l5.9-.8z" fill="#fff"/></svg>Favourite</div>
    </div>
    <div class="reply">
      <div class="ph"><svg width="38" height="42" viewBox="0 0 38 42"><circle cx="19" cy="13" r="9" fill="#d2d2d2"/><path d="M2 42c0-12 7-17 17-17s17 5 17 17z" fill="#d2d2d2"/></svg></div>
      <div class="box">Type your reply here...</div>
    </div>
  </article>

  <!-- thread 2 -->
  <article class="thread" style="top:504px">
    <div class="thread-bar">Thead #2</div>
    <div class="thread-body">
      <div class="avatar"><div role="img" aria-label="Member photo" style="background:linear-gradient(160deg,#a7a29d,#e7e7e7)"></div></div>
      <div class="thread-title">Lorem ipsum dolor sit amet conse ctetuer adipiscing elit.</div>
      <div class="meta">Posted by Martin Hale on <b>01/01/2014 - 15:32</b></div>
      <p class="excerpt">Lorem ipsum dolor sit actetuer adipiscing elitsed diam nonummy nibh euismodi tincidunt ut laoreet dolore magna aliquam erat volutpat. wisi eniminim veniamr quis nostrud exerci tation ullcorper suscipit lobortis nisl ut aliquip ea commodo consequat obortis nisl ut aliquip ea commodo consequat.</p>
      <div class="more">READ MORE »</div>
    </div>
    <div class="stats">
      <div class="stat" style="left:13px"><svg width="22" height="13" viewBox="0 0 22 13"><path d="M1 6.5C5 0 17 0 21 6.5 17 13 5 13 1 6.5z" fill="#3a5577"/><circle cx="11" cy="6.5" r="3.2" fill="#ebebeb"/><circle cx="11" cy="6.5" r="1.8" fill="#3a5577"/></svg>250 views</div>
      <div class="stat" style="left:118px"><svg width="19" height="17" viewBox="0 0 19 17"><path d="M1 1h17v11H7l-4 4v-4H1z" fill="#3a5577"/><path d="M4 4.5h11M4 8h8" stroke="#ebebeb" stroke-width="1.4"/></svg>12 replies</div>
      <div class="act" style="left:335px;width:81px"><svg width="14" height="11" viewBox="0 0 14 11"><path d="M6 0L0 5l6 5V7c4 0 6 1 8 4 0-5-3-7-8-7z" fill="#fff"/></svg>Reply</div>
      <div class="act" style="left:422px;width:85px"><svg width="15" height="15" viewBox="0 0 15 15"><circle cx="3" cy="7.5" r="2.3" fill="#fff"/><circle cx="12" cy="2.5" r="2.3" fill="#fff"/><circle cx="12" cy="12.5" r="2.3" fill="#fff"/><path d="M3 7.5l9-5M3 7.5l9 5" stroke="#fff" stroke-width="1.5"/></svg>Share</div>
      <div class="act" style="left:513px;width:103px"><svg width="17" height="16" viewBox="0 0 17 16"><path d="M8.5 0l2.6 5.3 5.9.8-4.3 4.1 1 5.8-5.2-2.8-5.2 2.8 1-5.8L0 6.1l5.9-.8z" fill="#fff"/></svg>Favourite</div>
    </div>
    <div class="reply">
      <div class="ph"><svg width="38" height="42" viewBox="0 0 38 42"><circle cx="19" cy="13" r="9" fill="#d2d2d2"/><path d="M2 42c0-12 7-17 17-17s17 5 17 17z" fill="#d2d2d2"/></svg></div>
      <div class="box">Type your reply here...</div>
    </div>
  </article>

  <div class="dropdown" style="left:7px;top:81px;width:75px">
    <div class="on">Recent</div>
    <div>Popular</div>
  </div>
  <div class="dropdown" style="left:36px;top:650px;width:103px">
    <div class="on">View profile</div>
    <div>View all posts</div>
  </div>
</main>

<div class="top-tab">TOP</div>
<footer class="site-footer">
  <div class="copy">Copyright © 2014 Ticker Commons.</div>
  <div class="social" style="left:961px;background:var(--blue)"></div>
  <div class="social" style="left:989px;background:#9a9a9a"></div>
  <div class="social" style="left:1017px;background:#b4b4b4"></div>
  <div class="social" style="left:1046px;background:#a8a8a8"></div>
</footer>

</body>
</html>
```